Business Card Design Project

We need a business card design for a consultancy called 'Maple Ridge'. The design should communicate innovation and professionalism. The colors used should complement our logo. Please include source files for winning design.
Updates

Industry/Entity Type

Business

Colors

Designer to choose colors to be used in the design.

Requirements
Must have
• Card size should be 85mm x 50mm. The back side of the card should be the logo on a black background. The front side should display the name 'Maple Ridge' along with standard information. The front's design should graphically complement the back.
Nice to have
• Any graphical elements in the front the complement the back side (with the logo on a black background) would be a plus.

```html
<!DOCTYPE html>
<html lang="en">
<head>
<meta charset="utf-8">
<title>Maple Ridge – Business Cards</title>
<link rel="stylesheet" href="https://fonts.googleapis.com/css2?family=Cinzel:wght@600&family=Questrial&display=swap">
<style>
  :root {
    --bg: #2b2b2b;
    --card-black: #121212;
    --gold: #f0b860;
    --cream: #f7f0a4;
    --amber: #f0a24a;
    --orange: #e0581c;
    --ink: #1a1a1a;
    --ink-soft: #5a4a30;
  }
  * { margin: 0; padding: 0; box-sizing: border-box; }
  html, body { width: 1200px; height: 1000px; overflow: hidden; background: var(--bg); }
  .canvas {
    position: relative; width: 1200px; height: 1000px;
    display: flex; flex-direction: column; align-items: center; justify-content: center; gap: 40px;
  }
  .card {
    position: relative; width: 560px; height: 330px; border-radius: 16px; overflow: hidden;
    box-shadow: 0 10px 24px rgba(0,0,0,0.45);
  }
  /* Back side */
  .card--back { background: var(--card-black); }
  .brand-mark {
    position: absolute; left: 312px; top: 60px; width: 154px; height: 154px; border-radius: 50%;
    background: linear-gradient(180deg, var(--cream), var(--amber));
  }
  .brand-name {
    position: absolute; left: 389px; top: 222px; transform: translateX(-50%);
    font-family: "Cinzel", serif; font-weight: 600; font-size: 32px; color: var(--gold);
    white-space: nowrap; letter-spacing: 0.5px;
  }
  .web-bar {
    position: absolute; left: 0; top: 224px; width: 224px; height: 27px;
    border-radius: 0 6px 6px 0;
    background: linear-gradient(90deg, var(--orange), var(--amber) 40%, var(--cream));
    font-family: "Questrial", sans-serif; font-size: 15px; color: var(--ink);
    display: flex; align-items: center; justify-content: flex-end; padding-right: 12px;
  }
  /* Front side */
  .card--front {
    background: linear-gradient(90deg, var(--cream) 0%, #f4d888 30%, var(--amber) 65%, var(--orange) 100%);
    font-family: "Questrial", sans-serif; color: var(--ink-soft);
  }
  .front-name {
    position: absolute; left: 38px; top: 28px;
    font-family: "Cinzel", serif; font-weight: 600; font-size: 32px; color: var(--ink);
  }
  .info { position: absolute; font-size: 14px; line-height: 19px; }
  .info--address { left: 38px; top: 78px; }
  .info--phone { left: 310px; top: 78px; }
  .info--direct { left: 310px; top: 218px; }
  .person-bar {
    position: absolute; left: 0; top: 216px; width: 275px; height: 24px;
    background: var(--ink); border-radius: 0 6px 6px 0;
    color: var(--cream); font-size: 16px; font-weight: 700; letter-spacing: 0.5px;
    display: flex; align-items: center; padding-left: 38px;
  }
  .person-title { position: absolute; left: 38px; top: 246px; font-size: 14px; }
</style>
</head>
<body>
<main class="canvas">
  <section class="card card--back" aria-label="Card back">
    <div class="brand-mark"></div>
    <div class="brand-name">Maple Ridge</div>
    <div class="web-bar">www.mapleridgeco.net</div>
  </section>

  <section class="card card--front" aria-label="Card front">
    <h1 class="front-name">Maple Ridge</h1>
    <p class="info info--address">Head Office: Elm Tower 4210.<br>No.27/B Harbor Lane, Westfield</p>
    <p class="info info--phone">Tel:&nbsp; + 10(555) 240 16 30<br>Fax: + 10(555) 240 16 31</p>
    <div class="person-bar">JANE MARLOW</div>
    <p class="person-title">Director</p>
    <p class="info info--direct">jane_marlow@mapleridgeco.net<br>0150 5550 1234</p>
  </section>
</main>
</body>
</html>
```